3 Beispiel-Abbildungen für shop Kategorien
Zielgruppe
Entscheider und Ihre AssistentInnen im Marketing / Vertrieb von Firmen aller Branchen und Größen
Aufgabenstellung
Für einen B2B shop benötigen wir Piktogramme / Abbildungen / Grafiken für Kategorien (Produktlinien, Produktgruppen, Dienstleistungen...)
Mit einer eigenständig entwickelten Navi führen wir den Kunden direkt zu den Produkten und zeigen dabei immer die Alternativen. Viel Wert haben wir auf die Aktikelbeschreibungen und Abbildungen gelegt. Fuchsgrund.de will ein Fachgeschäft im Internet sein.
Die Abbildungen sollen aus einem Guß sein und zum CI der Seite passen. Da es am Ende ca. 300 Abbildungen sein werden, (mache sind doppelt, viele unterscheiden sich nur wenig) muss das Konzept einfach sein. Die Gesamt-Kosten sollten sich taxieren lassen und die Realisiierung sollte in insgesamt 8-12 Wochen hochgeladen sein.
Der Designer / die Desingerin sollte davon ausgehen, dass auch die Folgeaufträge zu machen (oder zu vergeben) sind.

```html
<!DOCTYPE html>
<html lang="de">
<head>
<meta charset="utf-8">
<title>Shop Kategorien – Welt-Edition</title>
<link rel="stylesheet" href="https://fonts.googleapis.com/css2?family=Open+Sans:wght@400;600&family=Arimo:wght@400;700&display=swap">
<style>
  :root{
    --page-blue:#0a77ac;
    --navy-top:#0f2a47;
    --navy-bottom:#1d5582;
    --green-top:#8cc152;
    --green-bottom:#6aa52f;
    --green-accent:#7cb342;
    --pale-green:#e6f1da;
    --white:#ffffff;
    --text:#333333;
    --rule:#d8d8d8;
    --dots:#9a9a9a;
    --faint:rgba(255,255,255,.22);
  }
  *{box-sizing:border-box;margin:0;padding:0}
  html,body{width:1200px;height:481px;overflow:hidden;background:var(--page-blue)}
  body{position:relative;font-family:"Arimo",Arial,sans-serif;color:var(--text)}
  .column{position:absolute;top:14px}
  .col-products{left:19px;width:298px;height:467px;background:var(--white)}
  .col-maps{left:324px;width:298px;height:467px;background:var(--white)}
  .col-detail{left:628px;width:560px;height:443px;background:var(--white)}

  .hero{position:relative;height:179px;overflow:hidden;
    background:linear-gradient(180deg,var(--navy-top),var(--navy-bottom));
    border-bottom:3px solid var(--green-accent)}
  .hero-art{position:absolute;left:50%;top:12px;transform:translateX(-50%);
    width:240px;height:110px;border-radius:40%;
    background:radial-gradient(ellipse at center,#74d63a 0%,#4fae24 45%,rgba(79,174,36,0) 72%)}
  .col-detail .hero-art{left:auto;right:10px;transform:none;width:330px;height:150px;top:0}
  .hero-title{position:absolute;left:10px;bottom:8px;font-family:"Open Sans",sans-serif;
    font-size:17px;letter-spacing:1px;color:var(--white)}
  .hero-headline{position:absolute;left:20px;top:94px;font-family:"Open Sans",sans-serif;
    font-size:29px;letter-spacing:1.5px;color:var(--white)}
  .hero-word{position:absolute;font-family:"Open Sans",sans-serif;color:var(--faint);letter-spacing:1px}

  .band{height:26px;line-height:26px;padding-left:9px;color:var(--white);font-weight:700;font-size:15px;
    background:linear-gradient(180deg,var(--green-top),var(--green-bottom))}
  .nav-item{height:71px;line-height:71px;padding-left:9px;font-size:13.5px;border-bottom:1px solid var(--rule)}
  .nav-item.active{background:var(--pale-green);border-bottom:none;position:relative;height:69px}
  .nav-item.active svg{position:absolute;right:10px;top:26px}
  .nav-fill{height:20px;background:var(--pale-green)}

  .tab-band{position:relative;height:26px;background:linear-gradient(180deg,var(--green-top),var(--green-bottom))}
  .tab{position:absolute;left:3px;top:2px;height:24px;padding:0 6px;line-height:24px;font-size:14.5px;
    color:#111;background:#f3f8ec}
  .tab svg{position:absolute;left:26px;top:24px}
  .listing{padding:0 12px}
  .dotted{border-top:1px dotted var(--dots)}
  .product{position:relative;height:142px;margin-top:39px}
  .thumb{position:absolute;left:35px;top:20px;width:88px;height:42px;border-radius:30%;
    background:radial-gradient(ellipse,#f08a1c 0%,#f6b04a 55%,rgba(246,176,74,0) 75%)}
  .product-name{position:absolute;left:167px;top:17px;font-size:18px;font-weight:700;color:var(--green-accent)}
  .product-meta{position:absolute;left:167px;top:43px;font-size:14.5px;font-weight:700}
  .more{position:absolute;left:14px;top:86px;font-size:15px;font-weight:700;color:#444}
  .pager{display:flex;justify-content:space-between;padding:17px 10px 0 2px;font-size:14.5px}
</style>
</head>
<body>
  <section class="column col-products">
    <div class="hero">
      <div class="hero-art" role="img" aria-label="Grüne Weltkarte auf dunkelblauem Grund"></div>
      <div class="hero-title">Landkarten und Zubehör</div>
    </div>
    <div class="band">Software</div>
    <div class="nav-item">GeoPlaner</div>
    <div class="nav-item">LIVE-DEMO</div>
    <div class="nav-item">SpotFinder (Standortsuche)</div>
    <div class="band">Daten</div>
    <div class="nav-fill"></div>
  </section>

  <section class="column col-maps">
    <div class="hero">
      <div class="hero-art" role="img" aria-label="Grüne Weltkarte auf dunkelblauem Grund"></div>
      <div class="hero-title">Wandkarten</div>
    </div>
    <div class="band">Marktdaten und Geodaten (GIS)</div>
    <div class="nav-item active">Marktdaten + Geodaten (GIS)
      <svg width="12" height="18" viewBox="0 0 12 18"><path d="M0 0L12 9L0 18Z" fill="#7cb342"/></svg>
    </div>
  </section>

  <section class="column col-detail">
    <div class="hero">
      <div class="hero-art" role="img" aria-label="Grüne Weltkarte auf dunkelblauem Grund"></div>
      <span class="hero-word" style="left:74px;top:22px;font-size:16px">Asien</span>
      <span class="hero-word" style="left:162px;top:40px;font-size:16px">Afrika</span>
      <span class="hero-word" style="left:46px;top:62px;font-size:22px">Europa</span>
      <span class="hero-word" style="left:62px;top:124px;font-size:13px">Australien</span>
      <span class="hero-word" style="left:206px;top:120px;font-size:20px">Amerika</span>
      <div class="hero-headline">Welt-Edition</div>
      <div class="hero-title">Welt-Edition</div>
    </div>
    <div class="tab-band">
      <div class="tab">Kategorie 1
        <svg width="20" height="10" viewBox="0 0 20 10"><path d="M0 0H20L10 10Z" fill="#7cb342"/></svg>
      </div>
    </div>
    <div class="listing">
      <div class="product dotted">
        <div class="thumb" role="img" aria-label="Orange Weltkarte der Marktdaten"></div>
        <div class="product-name">Marktdaten</div>
        <div class="product-meta">Nr.: &nbsp;· &nbsp;Größe:</div>
        <div class="more">mehr...</div>
      </div>
      <div class="dotted"></div>
      <div class="pager">
        <span>Zeige <b>1</b> bis <b>1</b> (von insgesamt <b>1</b> Artikeln)</span>
        <span>Seiten: &nbsp;<b>1</b></span>
      </div>
    </div>
  </section>
</body>
</html>
```